Flyer for photo scanning business

Hello,
I need a flyer created for my business that would be suitable for print, to drop in letterboxes in my local community.

I would like the flyer to convey very simply the services I offer which is scanning negatives, slides and VHS tapes to digital files.
Hopefully it can make it look like an easy process, as people are often daunted by the task of sorting through old photos so they don't always get around to having them scanned.

I have a pinned facebook post that can be used by the designer to reference my services. Pricing does not need to be included on the flyer.
http://facebook.com/brightvaleimaging

Target Market(s)

Parents & Grandparents

Requirements
Must have
• Must make my services look simple! Refer to pinned facebook post for detailed outline of my services.

I would like to flyer to point towards my contact details -
www.brightvale.com
Margot 0478 219 836

Colours in line with my logo/brand (uploaded to brief).
Nice to have
• Stock images of 35mm film negatives, 8mm film, VHS tapes, or Lumavert slides would be worth including. I have also uploaded a mockup of the USB sticks that I provide with digitised images.
Should not have
• no prices needed,

```html
<!DOCTYPE html>
<html lang="en">
<head>
<meta charset="utf-8">
<title>Brightvale Digital – Services Offer Flyer</title>
<link rel="stylesheet" href="https://fonts.googleapis.com/css2?family=Oswald:wght@300;400;500;600;700&family=Montserrat:wght@400;500&display=swap">
<style>
  :root {
    --brand-blue: #4863a8;
    --brand-blue-deep: #34509c;
    --ink: #1b1b1d;
    --paper: #ffffff;
    --stage: #e6e7ea;
    --text-dark: #222226;
  }
  * { margin: 0; padding: 0; box-sizing: border-box; }
  html, body { width: 1200px; height: 792px; overflow: hidden; }
  body { background: var(--stage); position: relative; font-family: "Montserrat", sans-serif; }

  .flyer {
    position: absolute; left: 331px; top: 16px;
    width: 537px; height: 760px;
    background: var(--paper); overflow: hidden;
    box-shadow: 0 6px 18px rgba(0,0,0,.18);
  }

  .hero-photo {
    position: absolute; left: 0; top: 0; width: 537px; height: 340px;
    background:
      radial-gradient(ellipse at 70% 45%, #d9d9d9 0%, #8c8c8c 30%, rgba(60,60,60,0) 55%),
      linear-gradient(160deg, #7b5b4c 0%, #a88470 35%, #b9a79c 60%, #5d4e49 100%);
  }

  .header-shape { position: absolute; left: 0; top: 0; }

  .brand {
    position: absolute; left: 14px; top: 22px;
    display: flex; align-items: center; gap: 9px;
  }
  .brand-dot { width: 36px; height: 36px; border-radius: 50%; background: var(--brand-blue); }
  .brand-name {
    font-family: "Montserrat", sans-serif; font-weight: 500;
    color: var(--brand-blue-deep); font-size: 17px; letter-spacing: 2.5px; line-height: 1.15;
  }

  .tagline-band { position: absolute; left: 0; top: 0; }
  .tagline {
    position: absolute; left: 278px; top: 382px; transform: translateY(-50%);
    font-family: "Oswald", sans-serif; font-weight: 300;
    color: #fff; font-size: 24px; line-height: 1.18;
  }

  .offer-box {
    position: absolute; left: 22px; top: 291px; width: 248px; height: 160px;
    background: var(--brand-blue); border-radius: 16px;
    color: #fff; font-family: "Oswald", sans-serif; text-align: center;
  }
  .offer-rule { position: absolute; left: 10px; right: 10px; display: flex; align-items: center; gap: 7px; }
  .offer-rule::before, .offer-rule::after { content: ""; flex: 1; height: 1.5px; background: #fff; }
  .offer-brand { top: 17px; font-size: 25px; font-weight: 600; line-height: 1; }
  .offer-title { position: absolute; left: 0; right: 0; top: 45px; font-size: 54px; font-weight: 700; line-height: 1; letter-spacing: .5px; text-shadow: 0 2px 3px rgba(0,0,0,.3); }
  .offer-sub { top: 105px; font-size: 38px; font-weight: 300; line-height: 1; }

  .service { position: absolute; left: 0; width: 537px; }
  .service-image {
    position: absolute; left: 12px; width: 100px; height: 103px;
    transform: rotate(-12deg); border-radius: 2px;
  }
  .service-image.negatives { background: linear-gradient(135deg, #2b2b2b 0%, #5b5b5b 40%, #c43b34 65%, #e2b83a 85%, #2f6fb5 100%); }
  .service-image.tapes { background: linear-gradient(135deg, #3d4d55 0%, #7c8b90 40%, #2a2a2a 65%, #b55a3b 85%, #2a2a2a 100%); }

  .service-body { position: absolute; left: 128px; width: 395px; }
  .service-heading {
    font-family: "Oswald", sans-serif; font-weight: 600; font-size: 27px; line-height: 1;
    color: var(--ink); display: inline-block; padding-bottom: 3px;
    border-bottom: 2px solid var(--brand-blue);
  }
  .service-heading .accent { color: var(--brand-blue); }
  .service-text { font-size: 9.8px; line-height: 1.25; color: var(--text-dark); margin-top: 9px; }
  .service-text + .service-text { margin-top: 12px; }

  .contact-band { position: absolute; left: 0; top: 0; }
  .contact-pill {
    position: absolute; left: 199px; top: 680px; width: 139px; height: 31px;
    background: var(--brand-blue-deep); border-radius: 16px;
    color: #fff; font-family: "Oswald", sans-serif; font-weight: 500; font-size: 18px;
    display: flex; align-items: center; justify-content: center; letter-spacing: .5px;
  }
  .contact-line {
    position: absolute; top: 735px; transform: translateY(-50%);
    font-family: "Oswald", sans-serif; font-weight: 500; font-size: 21px; color: #fff; white-space: nowrap;
  }
  .contact-line .label { color: var(--brand-blue); }
  .contact-phone { left: 39px; }
  .contact-web { left: 258px; }
</style>
</head>
<body>
  <main class="flyer">
    <div class="hero-photo" role="img" aria-label="Vintage silver film camera resting on old black and white photographs on a wooden table"></div>

    <svg class="header-shape" width="537" height="90" viewBox="0 0 537 90">
      <path d="M0 0 H292 C266 50 216 79 140 79 H0 Z" fill="#ffffff"/>
      <path d="M292 0 H310 C283 54 230 81 140 81 L140 79 C216 79 266 50 292 0 Z" fill="#34509c"/>
    </svg>

    <div class="brand">
      <span class="brand-dot"></span>
      <span class="brand-name">BRIGHTVALE<br>DIGITAL</span>
    </div>

    <svg class="tagline-band" width="537" height="425" viewBox="0 0 537 425">
      <path d="M0 328 H500 Q537 328 537 362 V415 H0 Z" fill="#1b1b1d"/>
      <rect x="278" y="417" width="259" height="2" fill="#4863a8"/>
      <rect x="0" y="417" width="15" height="2" fill="#4863a8"/>
    </svg>
    <p class="tagline">scanning negatives, slides<br>and VHS tapes to digital files</p>

    <section class="offer-box">
      <div class="offer-rule offer-brand">BRIGHTVALE</div>
      <div class="offer-title">SERVICES</div>
      <div class="offer-rule offer-sub">OFFER</div>
    </section>

    <section class="service" style="top:459px;">
      <div class="service-image negatives" style="top:3px;" role="img" aria-label="Collage of colourful film negatives and slides"></div>
      <div class="service-body" style="top:5px;">
        <h2 class="service-heading"><span class="accent">PHOTO NEGATIVE</span> SCANNING</h2>
        <p class="service-text">Digitising photo slides and negatives at 90cents per photo.</p>
        <p class="service-text">Your photos will be personally picked up and delivered back to your home with high resolution JPEG files on a USB drive</p>
      </div>
    </section>

    <section class="service" style="top:575px;">
      <div class="service-image tapes" style="top:0;" role="img" aria-label="Collage of vintage video cassette tapes"></div>
      <div class="service-body" style="top:5px;">
        <h2 class="service-heading"><span class="accent">VHS</span> DIGITISING</h2>
        <p class="service-text">Conversion of VHS tapes to computer friendly video files using high quality broadcast equipment.</p>
        <p class="service-text">Your tapes will be personally picked up and returned to your home with a USB drive.</p>
      </div>
    </section>

    <svg class="contact-band" width="537" height="760" viewBox="0 0 537 760">
      <path d="M0 760 V738 Q0 694 52 694 H485 Q537 694 537 738 V760 Z" fill="#1b1b1d"/>
    </svg>
    <div class="contact-pill">CONTACT US:</div>
    <p class="contact-line contact-phone"><span class="label">Phone:</span> 0478 219 836</p>
    <p class="contact-line contact-web"><span class="label">Website:</span> www.brightvale.com</p>
  </main>
</body>
</html>
```